Merrowind Flyer

A simple flyer that gets people attention
I have a attached a sample of what we use now and a picture we use
We service gas fireplaces and need a eye catching but not to cluttered flyer to promote our business. the cost per fireplace should be $60.00

Reason: Sorry for the delay We are out of town on holidays with sketchy internet service To frustrating to complete this project till I am back in a week Thank you for your patience Kind regards Dale

```html
<!DOCTYPE html>
<html lang="en">
<head>
<meta charset="utf-8">
<title>Merrowind Gas Services Flyer</title>
<link href="https://fonts.googleapis.com/css2?family=Oswald:wght@400;500;700&family=Open+Sans:wght@400;600;700&display=swap" rel="stylesheet">
<style>
  :root{
    --red:#c8161d;
    --red-dark:#8e1015;
    --maroon:#4e1712;
    --charcoal:#2b2b2b;
    --grey:#6b6b6b;
    --grey-box:rgba(70,66,64,.88);
    --ink:#2a2a2a;
    --white:#ffffff;
    --ember:#e0752a;
  }
  *{box-sizing:border-box;margin:0;padding:0}
  html,body{width:807px;height:1200px;overflow:hidden;background:#ececec}
  body{font-family:"Open Sans",sans-serif;color:var(--ink)}
  .flyer{position:relative;width:807px;height:1200px;background:var(--white);overflow:hidden}

  .hero{position:absolute;left:0;top:0;width:807px;height:600px;
    background:
      radial-gradient(ellipse at 50% 28%, #f6b04a 0%, var(--ember) 22%, #7a2c12 48%, transparent 70%),
      linear-gradient(180deg,#1e1410 0%,#3a2218 40%,#9c6a55 62%,#d6a48c 78%,#8a5b48 100%)}
  .hero-title{position:absolute;left:36px;top:36px;font-family:"Oswald",sans-serif;font-weight:700;
    font-size:50px;line-height:1;color:var(--white);letter-spacing:.5px;text-transform:uppercase}
  .hero-sub{position:absolute;left:38px;top:96px;width:560px;font-family:"Oswald",sans-serif;font-weight:500;
    font-size:24px;line-height:1.15;color:var(--white)}

  .facts{position:absolute;left:0;top:482px;width:588px;height:135px;display:flex;gap:8px;padding:0 0 0 8px}
  .fact{flex:1;background:var(--grey-box);color:var(--white);font-size:12.5px;line-height:1.35;
    text-align:center;padding:14px 12px;display:flex;align-items:center}

  .steps{position:absolute;left:0;top:640px;width:588px}
  .step{display:flex;align-items:flex-start;margin-bottom:18px}
  .step-num{flex:none;width:86px;height:118px;display:flex;align-items:center;justify-content:center;
    font-family:"Oswald",sans-serif;font-weight:700;font-size:64px;color:var(--white);background:var(--red)}
  .step:nth-child(2) .step-num{background:var(--maroon)}
  .step-text{padding:10px 22px 0 22px;font-size:13.5px;line-height:1.42;color:var(--ink)}
  .step-text .accent{color:var(--red);font-weight:700}
  .step-text strong{color:var(--red-dark)}

  .price-panel{position:absolute;left:604px;top:470px;width:203px;height:640px;background:var(--red);color:var(--white);padding:0 20px}
  .brand-box{position:absolute;left:22px;top:0;width:160px;height:140px;background:var(--red-dark);
    display:flex;align-items:center;justify-content:center;text-align:center;
    font-family:"Oswald",sans-serif;font-weight:700;font-size:22px;line-height:1.1;color:var(--white);text-transform:uppercase;
    border:3px solid var(--white)}
  .price-head{position:absolute;left:20px;top:166px;width:170px;font-family:"Oswald",sans-serif;font-weight:700;
    font-size:33px;line-height:1.08;text-transform:uppercase}
  .price-amount{display:block;font-size:56px;line-height:1.05;margin-top:4px}
  .price-note{position:absolute;left:20px;top:392px;width:168px;font-size:12px;line-height:1.35;font-weight:600}

  .footer{position:absolute;left:0;top:1110px;width:807px;height:90px;background:var(--red-dark);color:var(--white);
    display:flex;align-items:center;padding:0 26px}
  .footer-contact{width:220px;font-size:13px;line-height:1.35;font-weight:600}
  .footer-brand{flex:1;text-align:center;font-family:"Oswald",sans-serif;font-weight:700;font-size:26px;text-transform:uppercase;letter-spacing:.5px}
  .footer-phone{display:flex;align-items:center;gap:10px;font-family:"Oswald",sans-serif;font-weight:500;font-size:28px}
</style>
</head>
<body>
<div class="flyer">
  <div class="hero" role="img" aria-label="Photo of bare feet resting in front of a glowing gas fireplace"></div>
  <h1 class="hero-title">Merrowind Gas Services</h1>
  <p class="hero-sub">will be on site conducting gas fireplace safety inspections and maintenance.</p>

  <div class="facts">
    <p class="fact">We will require approximately 20 - 30 minutes to service each fireplace and require that the fireplace is cool to conduct the work.</p>
    <p class="fact">Fireplace could not be used 2hours of the technicians receive burns</p>
    <p class="fact">The National Home Energy Office states that all fireplaces require regular servicing.</p>
  </div>

  <div class="steps">
    <div class="step">
      <div class="step-num">1</div>
      <p class="step-text">Fireplace manufacturers recommend each unit be serviced annually by a qualified technician and insurance companies and Fire Departments are asking for reports regarding fireplace safety inspections and servicing.</p>
    </div>
    <div class="step">
      <div class="step-num">2</div>
      <p class="step-text">The service <span class="accent">Merrowind Gas Services</span> will provide will entail a thorough assessment of pilot, burner and valve operation, a door seal inspection, an inspection of the electrical circuits/repositioning of the logs, cleaning and adjustment of fan and controls, cleaning of the firebox and glass, a carbon monoxide test, testing of fittings for gas leaks and a complete operational test once the service is complete.</p>
    </div>
    <div class="step">
      <div class="step-num">3</div>
      <p class="step-text"><strong>The indication of the gas fireplace requires service is:</strong> (1) Cloudy film on glass, (2) Strong odors when fireplace is in operation, (3) Soot build up on glass, logs or exterior of building, (4) Tarnished/discolored brass, (5) Pilot light outages, (6) Main burner is not lighting consistently, (7) Delayed ignition, and (8) Flames are not evenly dispersed.</p>
    </div>
  </div>

  <aside class="price-panel">
    <div class="brand-box">Merrowind<br>Gas Services</div>
    <h2 class="price-head">The cost per fireplace should be <span class="price-amount">$60.00</span></h2>
    <p class="price-note">(Owners must have payment ready at time of inspection. Payment may be made in the form of cash, cheque or credit card)</p>
  </aside>

  <footer class="footer">
    <p class="footer-contact">For further information please contact Tessa at:</p>
    <p class="footer-brand">Merrowind Gas Services</p>
    <p class="footer-phone">
      <svg width="22" height="22" viewBox="0 0 24 24" aria-hidden="true"><path fill="#fff" d="M6.6 10.8a15.1 15.1 0 0 0 6.6 6.6l2.2-2.2c.3-.3.7-.4 1-.2 1.1.4 2.3.6 3.6.6.6 0 1 .4 1 1V20c0 .6-.4 1-1 1A17 17 0 0 1 3 4c0-.6.4-1 1-1h3.5c.6 0 1 .4 1 1 0 1.3.2 2.5.6 3.6.1.3 0 .7-.2 1z"/></svg>
      555.014.2290
    </p>
  </footer>
</div>
</body>
</html>
```